Alaska Outdoor Adventure Tour Company Flyer

We need a cutting edge flyer design that stands out above the rest. We are a tour company offering a variety of services. We would like two Dual sided flyers. One on Ice Fishing/Sledding/Snow Shoeing Only, One on Aurora viewing / Hot Springs Aurora Viewing, and the third we would like a to be a tri-fold flyer including all the activities listed above. We are trying to drive traffic to our website and phones for bookings. We of course want to push that we are the best most trusted tour/experience company in Alaska. We are on Roomnest as well as Voyalist and would like to include there logo as well as our own logo on all the flyers. I have attached photos of all of our competitors flyers. Here is our website https://www.brackenlodges.info/
Here is our listings on Roomnest
https://www.roomnest.example/outings/5820419?s=31&item_kind=4&entry_ref=7&ref_id=26150934

https://www.roomnest.example/outings/5827731?s=31&item_kind=4&entry_ref=7&ref_id=26150934

https://www.roomnest.example/outings/5849206?s=31&item_kind=4&entry_ref=7&ref_id=26150934

https://www.roomnest.example/outings/5851947?s=31&item_kind=4&entry_ref=7&ref_id=26150934

Here is our Friendwall Page
https://www.friendwall.example/Bracken-Lodges-517290846631270/?ref=saved

Target Market(s)

Japanese travelers and Chinese travelers. Our other market is travelers from New York, and California.

Industry/Entity Type

Tourism

Colors

Designer to choose colors to be used in the design.

Requirements
Must have
• Company Logo more prominent than the Roomnest and Voyalist logo. Website adress and phone number. Include of our best photos from our website or Roomnest page.
• Must be the long narrow flyer design. Either two sided design or tri-fold design
Nice to have
• Possibly some of the key titles in Japanese or Chinese. Hopping our flyers will stand out from the rest. bright new agey but Alaskan. Hopping for something really cool and cutting edge. PRICE MATCH GUARANTY

```html
<!DOCTYPE html>
<html lang="en">
<head>
<meta charset="utf-8">
<title>Bracken Lodges – Long Flyer</title>
<link rel="stylesheet" href="https://fonts.googleapis.com/css2?family=Raleway:wght@300;400;600;700&family=Noto+Sans+JP:wght@400;500&display=swap">
<style>
  :root{
    --stage:#cfcfcf;
    --ink-top:#0c0c0d;
    --ink-bottom:#48484b;
    --gold:#cdb887;
    --gold-light:#efe3bf;
    --gold-dark:#9c8553;
    --text:#cfcfcf;
    --text-dim:#b9b9b9;
    --tag-text:#3a3220;
  }
  *{box-sizing:border-box;margin:0;padding:0}
  html,body{width:1127px;height:1200px;overflow:hidden}
  body{background:var(--stage);position:relative;font-family:"Raleway",sans-serif}
  .flyer{position:absolute;top:38px;width:500px;height:1124px;overflow:hidden;
    background:linear-gradient(180deg,var(--ink-top) 0%,#151516 40%,var(--ink-bottom) 100%);
    box-shadow:0 10px 30px rgba(0,0,0,.35)}
  .flyer--front{left:42px}
  .flyer--back{left:585px}
  .top-band{position:absolute;left:0;top:0;width:100%;height:30px;
    background:linear-gradient(180deg,var(--gold-dark),rgba(156,133,83,.25))}
  .brand{position:absolute;left:0;right:0;top:92px;display:flex;justify-content:center;align-items:center;gap:14px;
    color:var(--gold);font-weight:600;font-size:36px}
  .brand__mark{width:16px;height:16px;border-radius:50%;background:var(--gold)}
  .tagline{position:absolute;left:20px;right:20px;top:212px;text-align:center;color:var(--text);font-weight:300;font-size:16px;line-height:22px}
  .partners{position:absolute;left:0;right:0;top:274px;display:flex;justify-content:center;gap:44px;color:var(--gold);font-weight:600;font-size:24px}
  .partners span{display:flex;align-items:center;gap:9px}
  .partners i{width:18px;height:18px;border-radius:50%;background:var(--gold);display:inline-block}
  .photo{position:absolute;border:2px solid var(--gold);overflow:hidden}
  .badge{position:absolute;width:62px;height:62px;border-radius:50%;
    background:radial-gradient(circle,var(--gold-light) 0 40%,var(--gold) 60%,var(--gold-dark) 100%);
    border:3px solid #222;z-index:2}
  .price{position:absolute;right:0;bottom:0;width:84px;height:30px;
    background:linear-gradient(90deg,transparent 0,var(--gold-dark) 18%,var(--gold-light) 100%);
    clip-path:polygon(16% 0,100% 0,100% 100%,0 100%);
    color:var(--tag-text);font-weight:700;font-size:16px;text-align:right;padding:5px 10px 0 0}
  .ice-a{background:linear-gradient(150deg,#5c87c9,#2d3b62 45%,#9ab6da)}
  .ice-b{background:linear-gradient(180deg,#b9c9e6,#e8eef8)}
  .ice-c{background:linear-gradient(160deg,#8da7cf,#d7dfe8 60%,#6e88b8)}
  .ice-d{background:linear-gradient(180deg,#d9dde8,#f1f2f6)}
  .ice-e{background:linear-gradient(140deg,#8fa9d6,#2f3d66 60%,#9cb4dd)}
  .ice-f{background:linear-gradient(170deg,#c0b5c5,#6b5a59 55%,#d9d2d6)}
  .sled-a{background:linear-gradient(170deg,#3b3a4b,#7a6f84 45%,#e8d6de 75%,#d24a22 90%)}
  .sled-b{background:linear-gradient(160deg,#6e6a58,#d0782f 55%,#b89a78)}
  .sled-c{background:linear-gradient(180deg,#9c8b79,#4b4448 50%,#d2642e)}
  .snow-a{background:linear-gradient(160deg,#2f5a3c,#9bb4c9 40%,#eef3f9)}
  .snow-b{background:linear-gradient(180deg,#a9bfd9,#e9eef6 60%,#b5c8dc)}
  .snow-c{background:linear-gradient(180deg,#7f98b4,#dfe7f1)}
  .section-title{position:absolute;left:21px;right:21px;color:var(--gold-light);font-weight:700;font-size:16px;letter-spacing:.3px;display:flex;justify-content:space-between}
  .section-title--center{justify-content:center;text-align:center}
  .jp{font-family:"Noto Sans JP",sans-serif;font-weight:400;color:var(--gold-light);font-size:16px}
  .jp-line{position:absolute;left:21px;right:21px;text-align:center}
  .body-copy{position:absolute;left:21px;right:21px;color:var(--text-dim);font-weight:300;font-size:14px;line-height:22px;text-align:justify;text-align-last:center}
  .call{position:absolute;left:0;right:0;top:1036px;height:30px;display:flex;align-items:center;justify-content:space-between}
  .call__band{width:80px;height:30px;background:linear-gradient(90deg,rgba(205,184,135,.15),rgba(205,184,135,.55))}
  .call__band--right{background:linear-gradient(90deg,rgba(205,184,135,.55),rgba(205,184,135,.15))}
  .call__text{color:var(--gold);font-weight:600;font-size:19px;letter-spacing:.5px}
  .site-band{position:absolute;left:0;right:0;bottom:0;height:46px;
    background:linear-gradient(90deg,#bfae80,var(--gold-light) 45%,#c8b587);
    color:#8f8a80;font-size:19px;letter-spacing:2px;text-align:center;line-height:46px}
</style>
</head>
<body>

<section class="flyer flyer--front">
  <div class="top-band" role="img" aria-label="Gold ornamental header band"></div>
  <div class="brand"><span class="brand__mark"></span><span>Bracken Lodges LLC</span></div>
  <p class="tagline">We are the best &amp; most trusted tour/experience company<br>in Alaska. Taking You Where You Want To Go</p>
  <div class="partners"><span><i></i>Voyalist</span><span><i></i>Roomnest</span></div>

  <div class="badge" style="left:14px;top:338px"></div>
  <div class="photo ice-a" style="left:21px;top:347px;width:307px;height:302px" role="img" aria-label="Guest holding a freshly caught trout inside the ice fishing tent">
    <div class="price">$128</div>
  </div>
  <div class="photo ice-b" style="left:340px;top:347px;width:139px;height:144px" role="img" aria-label="Guide drilling a hole in the lake ice with an auger"></div>
  <div class="photo ice-c" style="left:340px;top:505px;width:139px;height:144px" role="img" aria-label="Guest fishing through the ice by a heater in the ice house"></div>
  <div class="photo ice-d" style="left:21px;top:658px;width:148px;height:143px" role="img" aria-label="Guests crouched over a fishing hole on the ice"></div>
  <div class="photo ice-e" style="left:181px;top:658px;width:147px;height:143px" role="img" aria-label="Hands holding a caught fish beside an ice auger"></div>
  <div class="photo ice-f" style="left:340px;top:658px;width:139px;height:143px" role="img" aria-label="Guests enjoying hot drinks in the heated ice tent"></div>

  <h2 class="section-title" style="top:822px"><span>ALASKA ICE FISHING</span><span class="jp">アラスカ氷釣り</span></h2>
  <p class="body-copy" style="top:852px">If your idea of a perfect vacation includes experiencing and learning something new, look no further than our exclusive Ice Fishing Adventure. Join me ice fishing on Tanana lakes a few minutes from town. Everything needed will be provided. I will take you through the steps on how to catch Alaska Pike &amp; Grayling fish all from the warmth of the ice house. Snacks and hot chocolate will also be provided. GUARANTEED FISH</p>

  <div class="call"><span class="call__band" role="img" aria-label="Gold ornamental accent"></span><span class="call__text">CALL/TEXT - 907-555-0148</span><span class="call__band call__band--right" role="img" aria-label="Gold ornamental accent"></span></div>
  <div class="site-band">www.brackenlodges.info</div>
</section>

<section class="flyer flyer--back">
  <div class="top-band" role="img" aria-label="Gold ornamental header band"></div>

  <div class="badge" style="left:14px;top:42px"></div>
  <div class="photo sled-a" style="left:21px;top:52px;width:310px;height:300px" role="img" aria-label="Two guests holding orange sleds at the sledding hill at night">
    <div class="price">$45</div>
  </div>
  <div class="photo sled-b" style="left:340px;top:52px;width:139px;height:144px" role="img" aria-label="Orange sleds leaning against a pickup truck"></div>
  <div class="photo sled-c" style="left:340px;top:208px;width:139px;height:144px" role="img" aria-label="Group of guests carrying sleds up the hill"></div>

  <h2 class="section-title section-title--center" style="top:366px">THRILLING SLEDING ADVENTURE ALASKA</h2>
  <div class="jp-line jp" style="top:390px">スリリングスレッディングアドベンチャーアラスカ</div>
  <p class="body-copy" style="top:420px">Sledding is one of Alaska's most thrilling sports. We will meet at a local sledding hill located on the edge of town. We will go over sledding basics and how to steer the sled as your gliding down the hill. Once you feel comfortable you can enjoy racing your friends down the hill. This will be a memorable thrilling adventure you will remember forever!</p>

  <div class="badge" style="left:14px;top:578px"></div>
  <div class="photo snow-a" style="left:21px;top:588px;width:310px;height:276px" role="img" aria-label="Guests snowshoeing through a snowy spruce forest">
    <div class="price">$85</div>
  </div>
  <div class="photo snow-b" style="left:340px;top:588px;width:139px;height:132px" role="img" aria-label="Group of snowshoers resting in an open snowfield"></div>
  <div class="photo snow-c" style="left:340px;top:732px;width:139px;height:132px" role="img" aria-label="Snowshoe trail winding between birch trees"></div>

  <h2 class="section-title section-title--center" style="top:878px">SNOWSHOE ALASKA WILDERNESS ADVENTURE</h2>
  <div class="jp-line jp" style="top:902px">スノーシューアラスカワイルドネスアドベンチャー</div>
  <p class="body-copy" style="top:932px">Looking for a snow sport that will allow you to tour Alaska's beautiful landscape and scenery? Snowshoeing is a great way to explore the outdoors and experience all of Alaska's natural beauty. Enjoy a guided Snowshoe Journy through trails along the Tanana River and into a historic Alaska village on the hillside where you will see a living style of years past.</p>

  <div class="site-band">www.brackenlodges.info</div>
</section>

</body>
</html>
```